TDM accounting firm Canada - Modern and professional business cards

To use our existing logo and create a modern looking business card.
We are looking for double sided style.
Silver-metallic background - our logo in front (reverse side)
The reverse side from the attachment- big logo over silver-metallic background is preferred.
we would like to have a business card template that can be modified to change names, addresses, and other

Industry/Entity Type

Accounting

Contact Information for Business Card

Reverse side silver-metallic finish

Font styles to use
Sans Serif

Requirements
Must have
• Reverse side silver-metallic finish
• Modern look

```html
<!DOCTYPE html>
<html lang="en">
<head>
<meta charset="utf-8">
<title>TDM Business Card – Front and Reverse</title>
<link href="https://fonts.googleapis.com/css2?family=Saira:wght@400;500;700&display=swap" rel="stylesheet">
<style>
  :root {
    --canvas-bg: #e9e9ea;
    --card-white: #f4f4f4;
    --ink: #1e1e1e;
    --ink-soft: #3a3a3a;
    --brand-blue: #1c6fc0;
    --icon-bg: #1b1b1b;
    --metal-dark: #3b3b3d;
    --metal-darker: #2a2a2c;
    --silver-light: #e4e4e6;
    --silver-mid: #b9b9bd;
    --back-text: #ffffff;
  }
  * { box-sizing: border-box; margin: 0; padding: 0; }
  html, body { width: 1200px; height: 873px; overflow: hidden; }
  body {
    background: var(--canvas-bg);
    font-family: "Saira", sans-serif;
    display: flex;
    align-items: center;
    justify-content: center;
    gap: 60px;
  }
  .card {
    width: 525px;
    height: 300px;
    position: relative;
    overflow: hidden;
    box-shadow: 0 10px 28px rgba(0,0,0,.18);
  }

  /* Front */
  .card-front { background: var(--card-white); color: var(--ink); padding: 34px 38px; }
  .brand { display: flex; align-items: center; gap: 14px; }
  .brand-name {
    font-size: 36px; font-weight: 700; color: var(--brand-blue);
    line-height: 1; letter-spacing: 1px;
  }
  .brand-company {
    font-size: 12px; font-weight: 500; color: var(--brand-blue);
    line-height: 1.15; text-transform: uppercase; letter-spacing: .5px;
  }
  .person { margin-top: 24px; }
  .person-name { font-size: 21px; font-weight: 500; letter-spacing: .5px; }
  .person-title {
    font-size: 10.5px; text-transform: uppercase; letter-spacing: 1px;
    color: var(--ink-soft); margin-top: 2px;
  }
  .contact-web {
    position: absolute; left: 38px; bottom: 30px;
    font-size: 13px; line-height: 1.7;
  }
  .contact-phone {
    position: absolute; right: 38px; bottom: 30px;
    font-size: 17px; line-height: 1.55; letter-spacing: 1px;
  }
  .contact-row { display: flex; align-items: center; gap: 10px; }
  .contact-phone .contact-row { justify-content: flex-end; }
  .icon {
    width: 18px; height: 18px; background: var(--icon-bg);
    display: inline-flex; align-items: center; justify-content: center;
    flex: none;
  }
  .icon svg { width: 12px; height: 12px; }

  /* Reverse */
  .card-back {
    background:
      repeating-linear-gradient(90deg, rgba(255,255,255,.03) 0 1px, transparent 1px 3px),
      linear-gradient(160deg, var(--metal-dark), var(--metal-darker));
  }
  .back-artwork {
    position: absolute; left: 0; right: 0; bottom: 0; height: 42%;
    background: linear-gradient(160deg, var(--silver-light), var(--silver-mid));
  }
  .back-brand {
    position: absolute; left: 44px; top: 42px; color: var(--back-text);
  }
  .back-brand-name {
    font-size: 48px; font-weight: 700; line-height: 1; letter-spacing: 2px;
  }
  .back-tagline {
    font-size: 12px; font-weight: 400; letter-spacing: 1.5px; margin-top: 8px;
  }
</style>
</head>
<body>

  <section class="card card-front" aria-label="Business card front">
    <div class="brand">
      <span class="brand-name">TDM</span>
      <span class="brand-company">Tidemark<br>Professional<br>Corporation</span>
    </div>
    <div class="person">
      <p class="person-name">Marco Delgado CPA, CGA</p>
      <p class="person-title">Principal and Senior Consultant</p>
    </div>

    <div class="contact-web">
      <div class="contact-row">
        <span class="icon"><svg viewBox="0 0 12 12"><rect x="1" y="2.5" width="10" height="7" fill="none" stroke="#fff" stroke-width="1.2"/><path d="M1 3l5 4 5-4" fill="none" stroke="#fff" stroke-width="1.2"/></svg></span>
        <span>marco@tdm-cpa.com</span>
      </div>
      <div class="contact-row">
        <span class="icon"><svg viewBox="0 0 12 12"><circle cx="6" cy="6" r="4.5" fill="none" stroke="#fff" stroke-width="1.2"/><path d="M1.5 6h9M6 1.5c-2 2.5-2 6.5 0 9M6 1.5c2 2.5 2 6.5 0 9" fill="none" stroke="#fff" stroke-width="1"/></svg></span>
        <span>www.tdm-cpa.com</span>
      </div>
    </div>

    <div class="contact-phone">
      <div class="contact-row">
        <span>(780) 555-0142</span>
        <span class="icon"><svg viewBox="0 0 12 12"><rect x="2" y="1.5" width="8" height="9" fill="none" stroke="#fff" stroke-width="1.2"/><path d="M3.5 4h5" stroke="#fff" stroke-width="1"/></svg></span>
      </div>
      <div class="contact-row">
        <span>(780) 555-0187</span>
        <span class="icon"><svg viewBox="0 0 12 12"><path d="M3 1.5l2 2.5-1.2 1.2c.6 1.3 1.7 2.4 3 3L8 7l2.5 2-1 1.5C5.5 10.5 1.5 6.5 1.5 2.5z" fill="#fff"/></svg></span>
      </div>
    </div>
  </section>

  <section class="card card-back" aria-label="Business card reverse, silver metallic">
    <div class="back-artwork" role="img" aria-label="Brushed silver swoosh artwork across the lower part of the card"></div>
    <div class="back-brand">
      <p class="back-brand-name">TDM</p>
      <p class="back-tagline">SR&amp;ED • TAX • ACCOUNTING</p>
    </div>
  </section>

</body>
</html>
```